Lumen Ridge Puzzles Business Cards
Two-sided business cards
Professional
Pim Varlotte
Founder, KORV Fellow, Brellaquin MVP
pim@lumenridgepuzzles.example
www.lumenridgepuzzles.example
GPG Fingerprint: A2D1 5B09 F6C3 17E4 8D2A 40BC 9E71 3F58 C046
Logo to Use for Business Cards

```html
<!DOCTYPE html>
<html lang="en">
<head>
<meta charset="utf-8">
<title>Lumen Ridge Puzzles Stationery</title>
<link rel="stylesheet" href="https://fonts.googleapis.com/css2?family=Montserrat:wght@400;600;700&display=swap">
<style>
  :root {
    --navy: #1b2f78;
    --blue: #2a5fc0;
    --green: #7cc242;
    --ink: #333a48;
    --muted: #8a909c;
    --paper: #ffffff;
    --stage: #eef0f3;
    --black: #0d0f12;
    --ghost: #e6e9f1;
    --rule: #9aa2b0;
  }
  * { box-sizing: border-box; margin: 0; padding: 0; }
  html, body { width: 1200px; height: 552px; overflow: hidden; }
  body { background: var(--stage); font-family: "Montserrat", Arial, sans-serif; color: var(--ink); position: relative; }
  .sheet { position: absolute; background: var(--paper); box-shadow: 0 1px 4px rgba(0,0,0,.18); overflow: hidden; }
  .sheet svg.swoosh { position: absolute; }
  .brand { position: absolute; display: flex; align-items: center; gap: 5px; }
  .brand-mark { width: 9px; height: 9px; background: var(--green); }
  .brand-name { font-weight: 700; font-size: 7px; letter-spacing: .06em; color: var(--navy); text-transform: uppercase; white-space: nowrap; }
  .brand.on-dark .brand-name { color: #ffffff; }
  .ghost-seal { position: absolute; border-radius: 50%; background: var(--ghost); opacity: .7; }
  .footer-line { position: absolute; left: 0; right: 0; text-align: center; font-size: 4.5px; color: var(--muted); letter-spacing: .02em; }

  /* fax */
  .fax { left: 19px; top: 19px; width: 365px; height: 514px; }
  .fax-title { position: absolute; right: 14px; top: 20px; font-weight: 700; font-size: 9px; color: var(--ink); }
  .fax-table { position: absolute; left: 12px; top: 32px; width: 341px; border-collapse: collapse; font-size: 5.5px; }
  .fax-table td { border: 0.8px solid var(--rule); height: 14px; padding: 0 5px; }
  .fax-table td.label { width: 42px; }
  .fax-checks { position: absolute; left: 12px; top: 104px; width: 341px; display: flex; justify-content: space-between; font-size: 5px; }
  .fax-checks span { display: flex; align-items: center; gap: 3px; }
  .fax-checks i { width: 6px; height: 6px; border: 0.8px solid var(--ink); display: inline-block; }

  /* letterhead */
  .letterhead { left: 403px; top: 19px; width: 353px; height: 514px; }

  /* cards */
  .card { position: absolute; background: var(--black); box-shadow: 0 1px 4px rgba(0,0,0,.25); overflow: hidden; color: #d7dbe2; }
  .card-front { left: 773px; top: 19px; width: 206px; height: 120px; }
  .card-back { left: 996px; top: 19px; width: 185px; height: 120px; }
  .card-details { position: absolute; left: 100px; top: 40px; font-size: 4.6px; line-height: 1.55; }
  .card-details .person { font-weight: 700; font-size: 6.5px; color: #ffffff; }
  .card-details .role { color: var(--green); margin-bottom: 3px; }
  .card-back .back-web { position: absolute; left: 0; right: 0; bottom: 22px; text-align: center; font-size: 5px; color: #c9ced8; }
  .card-back .back-print { position: absolute; left: 0; right: 0; bottom: 12px; text-align: center; font-size: 3.6px; color: var(--muted); }

  /* envelopes */
  .envelope-front { left: 773px; top: 163px; width: 408px; height: 161px; }
  .env-return { position: absolute; left: 24px; top: 38px; font-size: 4.5px; line-height: 1.6; color: var(--muted); }
  .envelope-back { left: 773px; top: 348px; width: 408px; height: 185px; background: var(--black); }
</style>
</head>
<body>

<!-- Fax sheet -->
<section class="sheet fax">
  <div class="brand" style="left:14px;top:10px"><span class="brand-mark"></span><span class="brand-name">Lumen Ridge Puzzles</span></div>
  <div class="fax-title">FAX</div>
  <table class="fax-table">
    <tr><td class="label">To :</td><td></td><td class="label">From :</td><td></td></tr>
    <tr><td class="label">Fax :</td><td></td><td class="label">Pages :</td><td></td></tr>
    <tr><td class="label">Phone :</td><td></td><td class="label">Date :</td><td></td></tr>
    <tr><td class="label">Re :</td><td></td><td class="label">CC :</td><td></td></tr>
  </table>
  <div class="fax-checks">
    <span><i></i>Urgent</span><span><i></i>For Review</span><span><i></i>Please Comment</span><span><i></i>Please Reply</span><span><i></i>Please Recycle</span>
  </div>
  <div class="ghost-seal" style="left:120px;top:330px;width:125px;height:125px"></div>
  <div class="footer-line" style="top:482px">T: +1 555 014 2287 &nbsp;|&nbsp; pim@lumenridgepuzzles.example &nbsp;|&nbsp; www.lumenridgepuzzles.example</div>
  <svg class="swoosh" style="left:0;bottom:0" width="365" height="20" viewBox="0 0 365 20">
    <path d="M0 6 Q180 12 365 2 L365 20 L0 20 Z" fill="var(--navy)"/>
    <path d="M0 6 Q180 12 365 2 L365 5 Q180 15 0 9 Z" fill="var(--green)"/>
  </svg>
</section>

<!-- Letterhead -->
<section class="sheet letterhead">
  <div class="brand" style="left:14px;top:12px"><span class="brand-mark"></span><span class="brand-name">Lumen Ridge Puzzles</span></div>
  <svg class="swoosh" style="right:0;top:0" width="70" height="55" viewBox="0 0 70 55">
    <path d="M0 0 L70 0 L70 55 Q62 8 0 0 Z" fill="var(--navy)"/>
    <path d="M8 0 Q64 6 70 48 L70 55 Q62 10 0 0 Z" fill="var(--green)"/>
  </svg>
  <div class="ghost-seal" style="left:115px;top:325px;width:125px;height:125px"></div>
  <div class="footer-line" style="top:486px">T: +1 555 014 2287 &nbsp;|&nbsp; pim@lumenridgepuzzles.example &nbsp;|&nbsp; www.lumenridgepuzzles.example</div>
  <svg class="swoosh" style="left:0;bottom:0" width="70" height="55" viewBox="0 0 70 55">
    <path d="M0 0 Q8 47 70 55 L0 55 Z" fill="var(--navy)"/>
    <path d="M0 0 Q8 47 70 55 L62 55 Q6 45 0 8 Z" fill="var(--green)"/>
  </svg>
</section>

<!-- Business card front -->
<section class="card card-front">
  <div class="brand on-dark" style="left:12px;top:12px"><span class="brand-mark"></span><span class="brand-name">Lumen Ridge Puzzles</span></div>
  <div class="card-details">
    <div class="person">Pim Varlotte</div>
    <div class="role">Founder, KORV Fellow, Brellaquin MVP</div>
    <div>T: +1 555 014 2287</div>
    <div>pim@lumenridgepuzzles.example</div>
    <div>www.lumenridgepuzzles.example</div>
  </div>
  <svg class="swoosh" style="position:absolute;right:0;top:0" width="60" height="40" viewBox="0 0 60 40">
    <path d="M0 0 L60 0 L60 40 Q54 6 0 0 Z" fill="var(--blue)"/>
    <path d="M10 0 Q56 4 60 34 L60 40 Q54 7 0 0 Z" fill="var(--green)"/>
  </svg>
</section>

<!-- Business card back -->
<section class="card card-back">
  <div class="brand on-dark" style="left:50%;top:48px;transform:translateX(-50%)"><span class="brand-mark"></span><span class="brand-name">Lumen Ridge Puzzles</span></div>
  <div class="back-web">www.lumenridgepuzzles.example</div>
  <div class="back-print">GPG Fingerprint: A2D1 5B09 F6C3 17E4 8D2A 40BC 9E71 3F58 C046</div>
</section>

<!-- Envelope front -->
<section class="sheet envelope-front">
  <div class="brand" style="left:24px;top:16px"><span class="brand-mark"></span><span class="brand-name">Lumen Ridge Puzzles</span></div>
  <div class="env-return">T: +1 555 014 2287<br>pim@lumenridgepuzzles.example<br>www.lumenridgepuzzles.example</div>
  <div class="ghost-seal" style="left:292px;top:38px;width:90px;height:90px"></div>
  <svg class="swoosh" style="right:0;top:0" width="70" height="38" viewBox="0 0 70 38">
    <path d="M0 0 L70 0 L70 38 Q60 5 0 0 Z" fill="var(--navy)"/>
    <path d="M10 0 Q64 4 70 32 L70 38 Q60 6 0 0 Z" fill="var(--green)"/>
  </svg>
  <svg class="swoosh" style="left:0;bottom:0" width="80" height="48" viewBox="0 0 80 48">
    <path d="M0 0 Q8 42 80 48 L0 48 Z" fill="var(--navy)"/>
    <path d="M0 0 Q8 42 80 48 L70 48 Q6 40 0 8 Z" fill="var(--green)"/>
  </svg>
</section>

<!-- Envelope back -->
<section class="sheet envelope-back">
  <svg class="swoosh" style="left:0;top:0" width="408" height="185" viewBox="0 0 408 185">
    <path d="M0 0 L408 0 L408 20 L204 110 L0 20 Z" fill="#1a1d22"/>
    <path d="M0 20 L204 110 L408 20" fill="none" stroke="var(--blue)" stroke-width="1.2"/>
    <path d="M0 24 L204 114 L408 24" fill="none" stroke="var(--green)" stroke-width="0.8"/>
  </svg>
</section>

</body>
</html>
```